Modern Spot UV Business Card design

We are a relatively new real estate agency. We need a business card that reflects the professionalism and prestige of our company but is also modern and fresh, based around our logo.
We would love to utilise spot UV.
Happy to let the designers use their imagination and see what they come up with (we're not very creative, so have no ideas for you, sorry) :-)
We'd like one for each staff member, but I've just provided one staff members photo here to avoid confusion.

Target Market(s)

Families

Industry/Entity Type

Real Estate Agent

Contact Information for Business Card

Colin Varga - Director & Principal
Mobile: 0491 527 806
Email: colin.varga@vbrokers.example.com.au
Phone: (08) 7364 9150
Fax: (08) 7364 9182
www.vargabrokersrealestate.example.com.au

Font styles to use
Other font styles liked:
• Kabel Dm BT

Requirements
Must have
• Contact details, logo, photo, spot UV
Nice to have
• Modern interesting features that will make people comment. Nothing too feminine nor too masculine.
Should not have
• No houses! Nothing typical of a real estate agent.

```html
<!DOCTYPE html>
<html lang="en">
<head>
<meta charset="utf-8">
<title>Varga Brokers Real Estate – Business Card</title>
<link rel="stylesheet" href="https://fonts.googleapis.com/css2?family=Montserrat:wght@400;500;700&display=swap">
<style>
  :root {
    --backdrop: #e3e3e3;
    --card: #ffffff;
    --ink: #1c1c1c;
    --logo-ink: #3b3b3b;
    --accent-orange: #f08a1c;
    --accent-dot: #f5a623;
    --shadow: 0 10px 24px rgba(0,0,0,0.18);
  }
  html, body {
    margin: 0;
    width: 1200px;
    height: 1200px;
    overflow: hidden;
    background: var(--backdrop);
    font-family: "Montserrat", sans-serif;
  }
  .sheet {
    position: relative;
    width: 1200px;
    height: 1200px;
  }
  .card {
    position: absolute;
    left: 250px;
    width: 700px;
    height: 400px;
    background: var(--card);
    box-shadow: var(--shadow);
    overflow: hidden;
  }
  .card--front { top: 165px; }
  .card--back  { top: 635px; }

  /* Front */
  .front-pattern {
    position: absolute;
    inset: 0;
    background:
      radial-gradient(circle at 12% 30%, #2e6fd8 0%, transparent 45%),
      radial-gradient(circle at 25% 85%, #e0207f 0%, transparent 40%),
      radial-gradient(circle at 90% 15%, #f7d21c 0%, transparent 30%),
      linear-gradient(90deg, #2a8fe0 0%, #4a3fb0 22%, #c42a8c 45%, #e5302a 70%, #f57a1e 88%, #f7b21c 100%);
  }
  .front-disc {
    position: absolute;
    left: 100px;
    top: -45px;
    width: 490px;
    height: 490px;
    border-radius: 50%;
    background: var(--card);
    display: flex;
    align-items: center;
    justify-content: center;
  }
  .brand {
    display: flex;
    align-items: center;
    gap: 14px;
  }
  .brand-dot {
    width: 30px;
    height: 30px;
    border-radius: 50%;
    background: var(--accent-dot);
    flex: none;
  }
  .brand-name {
    margin: 0;
    font-size: 36px;
    font-weight: 700;
    color: var(--logo-ink);
    letter-spacing: -0.5px;
    line-height: 1.1;
  }

  /* Back */
  .back-pattern {
    position: absolute;
    left: 0;
    top: 0;
    width: 290px;
    height: 400px;
  }
  .identity {
    position: absolute;
    left: 36px;
    top: 162px;
    color: #ffffff;
    text-transform: uppercase;
  }
  .identity-name {
    margin: 0;
    font-size: 24px;
    font-weight: 700;
    letter-spacing: 1px;
  }
  .identity-role {
    margin: 4px 0 0;
    font-size: 15px;
    font-weight: 500;
  }
  .contact-list {
    position: absolute;
    left: 292px;
    top: 178px;
    margin: 0;
    padding: 0;
    list-style: none;
    font-size: 13.5px;
    font-weight: 500;
    color: var(--ink);
    text-transform: uppercase;
    line-height: 1.85;
  }
  .contact-web {
    color: var(--accent-orange);
    margin-top: 6px;
  }
</style>
</head>
<body>
<main class="sheet">

  <section class="card card--front" aria-label="Card front">
    <div class="front-pattern" role="img" aria-label="Overlapping translucent colour blobs shading from blue and purple through pink and red to orange and yellow"></div>
    <div class="front-disc">
      <div class="brand">
        <span class="brand-dot"></span>
        <p class="brand-name">Varga Brokers<br>Real Estate</p>
      </div>
    </div>
  </section>

  <section class="card card--back" aria-label="Card back">
    <svg class="back-pattern" viewBox="0 0 290 400" role="img" aria-label="Cluster of translucent pink, red and orange colour blobs">
      <defs>
        <linearGradient id="blob-fill" x1="0" y1="0" x2="0.3" y2="1">
          <stop offset="0" stop-color="#d92a9a"/>
          <stop offset="0.45" stop-color="#ec2f6c"/>
          <stop offset="0.75" stop-color="#ef4a2a"/>
          <stop offset="1" stop-color="#f7a21e"/>
        </linearGradient>
      </defs>
      <path d="M0 0 H230 C275 20 285 90 255 135 C290 175 285 240 240 265 C215 285 170 290 150 315 C130 345 110 375 60 400 H0 Z" fill="url(#blob-fill)"/>
    </svg>
    <div class="identity">
      <h1 class="identity-name">Colin Varga</h1>
      <p class="identity-role">Director &amp; Principal</p>
    </div>
    <ul class="contact-list">
      <li>Mobile: 0491 527 806</li>
      <li>colin.varga@vbrokers.example.com.au</li>
      <li>Phone: (08) 7364 9150</li>
      <li>Fax: (08) 7364 9182</li>
      <li class="contact-web">www.vargabrokersrealestate.example.com.au</li>
    </ul>
  </section>

</main>
</body>
</html>
```